Webdesign für B2B-Unternehmen
Zielgruppe
Wir sind im B2B Geschäft tätig und sind ein Spin Off der Firma www.planvo.com
Aufgabenstellung
Es soll sehr Übersichtlich und nicht zu verspielt sein. Unsere Potenziellen Kunden sollen sehr einfach und schnell an Ihr Ziel kommen

```html
<!DOCTYPE html>
<html lang="en">
<head>
<meta charset="utf-8">
<title>NORVEX – Secure IoT Solutions</title>
<link href="https://fonts.googleapis.com/css2?family=Lato:wght@400;700;900&display=swap" rel="stylesheet">
<style>
:root{
  --navy:#0a0f5c;
  --blue:#0c2b8e;
  --card:#0a2a86;
  --card-hi:#1553cc;
  --green:#22a53b;
  --lime:#2ec24a;
  --white:#ffffff;
  --muted:#c9d4f5;
}
*{margin:0;padding:0;box-sizing:border-box}
html,body{width:1200px;height:4060px;overflow:hidden}
body{position:relative;font-family:'Lato',sans-serif;color:var(--white);background:var(--green)}
.abs{position:absolute}
.band{position:absolute;left:0;width:1200px}
.edge{position:absolute;left:0;width:1200px;height:60px}
/* header */
.hero{top:0;height:590px;background:linear-gradient(180deg,#0a0c55 0%,#0b1a78 70%,#0d2a98 100%)}
.hero-art{left:0;top:0;width:1200px;height:560px;background:radial-gradient(ellipse at 50% 40%,rgba(40,90,200,.35),rgba(10,12,85,0) 70%)}
.brand{left:150px;top:38px;font-size:34px;font-weight:700;letter-spacing:6px;color:var(--lime);display:flex;align-items:center;gap:12px}
.brand i{width:14px;height:14px;background:var(--lime);display:block}
.phone{left:836px;top:0;width:224px;height:42px;background:var(--card-hi);border-bottom:3px solid var(--lime);border-radius:0 0 6px 18px;display:flex;align-items:center;justify-content:center;gap:12px;font-size:20px;font-weight:700;letter-spacing:1px}
.nav-link{position:absolute;top:68px;width:160px;text-align:center;font-size:15px;font-weight:700;letter-spacing:1.5px;color:var(--white);text-decoration:none;white-space:nowrap}
.nav-link.active{color:var(--lime)}
.hero-title{left:0;width:1200px;top:250px;text-align:center;font-size:32px;font-weight:900;color:var(--lime)}
.hero-text{left:330px;width:540px;top:298px;text-align:center;font-size:16px;line-height:21px}
.btn-outline{border:2px solid var(--white);color:var(--white);font-size:14px;display:flex;align-items:center;justify-content:center}
.hero-btn{left:542px;top:383px;width:116px;height:34px}
/* features */
.feature{top:662px;width:282px;height:216px;background:var(--card);text-align:center;padding-top:28px}
.feature.hi{background:var(--card-hi);height:220px}
.feature h3{font-size:18px;font-weight:900;margin:12px 0 16px}
.feature p{font-size:12px;line-height:19px;padding:0 18px}
.video{left:150px;top:908px;width:900px;height:390px;background:linear-gradient(135deg,#0f2a7a,#1b2f8e 45%,#2a2a88 75%,#13206e)}
.play{left:556px;top:1048px;width:88px;height:88px;border-radius:50%;background:var(--green);border:3px solid #0a1a5a;box-shadow:0 0 0 3px #3b5bc6}
.video-label{left:0;width:1200px;top:1144px;text-align:center;font-size:18px}
/* welcome */
.blue-a{top:1340px;height:860px;background:var(--blue)}
.welcome-img{left:155px;top:1481px;width:390px;height:312px;background:linear-gradient(135deg,#1a2a5a,#0a0f2a 60%,#20306a);clip-path:polygon(12% 0,97% 0,100% 100%,0 100%)}
.welcome-accent{left:492px;top:1581px;width:52px;height:212px;background:var(--lime);clip-path:polygon(60% 0,100% 100%,0 100%)}
.welcome h2{left:585px;top:1497px;font-size:26px;font-weight:700;position:absolute}
.welcome p{position:absolute;left:585px;width:470px;font-size:12.5px;line-height:19.5px;color:var(--muted)}
.btn-line{border:1.5px solid #3e6bd8;color:var(--white);font-size:13px;display:flex;align-items:center;justify-content:center}
.sec-title{left:0;width:1200px;text-align:center;font-size:26px;font-weight:700}
.sec-title span{color:var(--lime)}
.solution{width:174px;height:174px;border-radius:50%;background:var(--white);border:5px solid var(--blue);box-shadow:0 0 0 3px var(--white)}
.solution .ring{position:absolute;inset:8px;border-radius:50%;background:var(--blue);display:flex;flex-direction:column;align-items:center;justify-content:center;gap:8px;font-size:16px;font-weight:700;text-align:center;line-height:19px}
/* news */
.news-card{top:2324px;width:429px;height:267px}
.news-card .date{position:absolute;left:20px;bottom:62px;font-size:11px}
.news-card .title{position:absolute;left:20px;right:20px;bottom:16px;font-size:14.5px;font-weight:700;line-height:18px}
.btn-solid{background:var(--card);color:var(--white);font-size:14px;font-weight:700;display:flex;align-items:center;justify-content:center}
/* roadmap */
.blue-b{top:2700px;height:690px;background:var(--blue)}
.map{left:260px;top:2790px;width:680px;height:330px;background:radial-gradient(ellipse,rgba(60,110,220,.35),rgba(12,43,142,0) 70%)}
.step{top:3006px;width:96px;text-align:center}
.step .when{font-size:14px;font-weight:700;white-space:nowrap}
.step .what{font-size:11px;line-height:12.5px;margin:28px auto 0;width:72px;color:var(--muted)}
.timeline{left:158px;top:3158px;width:884px;height:2px;background:#5474c8}
.dot{width:12px;height:12px;border-radius:50%;border:2px solid #8aa2e0;background:var(--blue);top:3153px}
.badge{width:76px;height:76px;border-radius:50%;background:radial-gradient(circle at 40% 35%,#ffffff,#dfe6ef 70%,#b8c6d6);border:4px solid #7fd0d8;top:3195px;display:flex;align-items:center;justify-content:center}
.badge b{width:26px;height:26px;border:2.5px solid var(--green);border-radius:50%}
/* certs */
.cert{top:3502px;width:100px;text-align:center;font-size:14px}
.cert .mark{width:58px;height:58px;margin:0 auto 10px;border:3px solid #cfeed6;border-radius:4px}
.cert .mark.round{border-radius:50%}
/* footer */
.footer{top:3655px;height:345px;background:var(--blue)}
.fcol{top:3766px}
.fcol h4{font-size:14px;font-weight:900;color:var(--lime);margin-bottom:22px}
.fcol a{display:block;font-size:13px;line-height:23px;color:var(--muted);text-decoration:none}
.social{top:3810px;width:38px;height:38px;border-radius:50%;border:3px solid var(--white)}
.bottom{top:3998px;height:62px;background:var(--green);font-size:13px}
.bottom nav{position:absolute;left:148px;top:22px;display:flex;gap:22px}
.bottom nav a{color:var(--white);text-decoration:none}
.bottom .copy{position:absolute;right:148px;top:22px}
</style>
</head>
<body>

<!-- hero -->
<section class="band hero">
  <div class="abs hero-art" role="img" aria-label="Network lines connecting two people using phones over a city skyline"></div>
  <div class="abs brand"><i></i>NORVEX</div>
  <div class="abs phone">
    <svg width="20" height="20" viewBox="0 0 24 24" fill="none" stroke="#fff" stroke-width="2"><path d="M5 3h4l2 5-3 2a12 12 0 0 0 6 6l2-3 5 2v4a2 2 0 0 1-2 2A18 18 0 0 1 3 5a2 2 0 0 1 2-2z"/></svg>
    555 014 2290
  </div>
  <nav>
    <a class="nav-link active" style="left:470px" href="#">HOME</a>
    <a class="nav-link" style="left:618px" href="#">PRODUCTS ⌄</a>
    <a class="nav-link" style="left:780px" href="#">SOLUTIONS ⌄</a>
    <a class="nav-link" style="left:930px" href="#">CONTACT</a>
  </nav>
  <h1 class="abs hero-title">Go further with secure IoT solutions</h1>
  <p class="abs hero-text">Lorem ipsum dolor sit amet, vero partem aliquando te quo, vis cu tempor legimus ocurreret, labore utamur cum eu.</p>
  <a class="abs btn-outline hero-btn">Learn More</a>
</section>
<svg class="edge" style="top:555px" viewBox="0 0 1200 60" preserveAspectRatio="none"><polygon fill="#22a53b" points="0,18 60,12 110,22 170,10 230,26 300,14 360,30 420,20 470,34 520,22 560,40 600,28 640,36 700,22 760,30 820,14 880,26 940,12 1000,24 1060,10 1120,22 1200,12 1200,60 0,60"/></svg>

<!-- features -->
<div class="abs feature" style="left:153px">
  <svg width="50" height="54" viewBox="0 0 50 54" fill="none" stroke="#2ec24a" stroke-width="3"><path d="M25 3 45 10v16c0 13-9 21-20 25C14 47 5 39 5 26V10z" stroke="#2f7fe0"/><circle cx="25" cy="26" r="10"/><path d="m20 26 4 4 7-8"/></svg>
  <h3>SECURE</h3>
  <p>We've securely managed over 60bn data records in over 70 countries and are 1 of only 6 certified full eSIM providers in the world.</p>
</div>
<div class="abs feature hi" style="left:460px">
  <svg width="54" height="54" viewBox="0 0 54 54" fill="none" stroke="#fff" stroke-width="5"><circle cx="27" cy="27" r="14"/><path d="M27 5v8M27 41v8M5 27h8M41 27h8M11 11l6 6M37 37l6 6M11 43l6-6M37 17l6-6"/></svg>
  <h3>OPTIMISE</h3>
  <p>We offer a complete solution which is noticeably faster to market, more responsive and cost-effective than most.</p>
</div>
<div class="abs feature" style="left:768px">
  <svg width="54" height="54" viewBox="0 0 54 54" fill="none" stroke-width="3"><circle cx="30" cy="24" r="17" stroke="#2ec24a"/><text x="22" y="30" font-size="15" font-weight="700" fill="#2ec24a" stroke="none" font-family="Lato,sans-serif">24</text><path d="M6 22c0 14 12 27 26 28l3-6-6-3-3 3c-5-3-9-7-12-12l3-3-3-6z" fill="#2f7fe0" stroke="none"/></svg>
  <h3>SUPPORT</h3>
  <p>We work closely with you, to provide the competitive edge to stay ahead and drive your digital transformation.</p>
</div>

<div class="abs video" role="img" aria-label="Connected car dashboard with digital gauges"></div>
<div class="abs play"><svg width="82" height="82" viewBox="0 0 82 82"><polygon points="33,24 60,41 33,58" fill="#fff"/></svg></div>
<div class="abs video-label">Watch Video</div>

<!-- welcome + solutions -->
<section class="band blue-a"></section>
<svg class="edge" style="top:1335px" viewBox="0 0 1200 60" preserveAspectRatio="none"><polygon fill="#22a53b" points="0,0 1200,0 1200,16 1140,24 1080,12 1020,26 960,16 900,30 840,20 780,34 720,24 660,38 600,26 540,36 480,22 420,32 360,18 300,28 240,14 180,26 120,16 60,24 0,14"/></svg>

<div class="abs welcome-img" role="img" aria-label="Hand touching a glowing digital interface on a tablet"></div>
<div class="abs welcome-accent"></div>
<div class="welcome">
  <h2>Welcome to NORVEX</h2>
  <p style="top:1550px">Id qui legere propriae, erat integre aliquando his id. Id noluisse corrumpit usu, sint assum eos no. Ne viderer mediocrem consequuntur sed. Has melius virtute an.</p>
  <p style="top:1608px">Lorem ipsum dolor sit amet, vero partem aliquando te quo, vis cu tempor legimus ocurreret, labore utamur cum eu. Ne has tamquam incorrupte. Eos at falli comprehensam, facete euripidis id pro, prima dictas feugiat qui ex. Ex duis dicat iusto mea. Illud delenit sapientem nam at, simul meliore his ei. Cum cu modus dolorum maiestatis, usu iudico quodsi ne.</p>
  <a class="abs btn-line" style="left:585px;top:1725px;width:112px;height:38px">Learn More</a>
</div>

<h2 class="abs sec-title" style="top:1876px"><span>NORVEX</span> Solutions and Products</h2>
<div class="abs solution" style="left:186px;top:1939px"><div class="ring">
  <svg width="32" height="42" viewBox="0 0 32 42" fill="none" stroke="#fff" stroke-width="2.5"><path d="M3 3h18l8 8v28H3z"/><rect x="9" y="16" width="14" height="16"/><path d="M16 16v16M9 24h14"/></svg>SIM</div></div>
<div class="abs solution" style="left:402px;top:1939px"><div class="ring">
  <svg width="60" height="40" viewBox="0 0 60 40" fill="none" stroke="#fff" stroke-width="3"><circle cx="30" cy="22" r="7"/><path d="M18 10a18 18 0 0 1 24 0M22 15a11 11 0 0 1 16 0M8 12v20M48 14h10M53 14v18"/></svg>IoT</div></div>
<div class="abs solution" style="left:621px;top:1939px"><div class="ring">
  <svg width="54" height="44" viewBox="0 0 54 44" fill="none" stroke="#fff" stroke-width="3"><path d="M4 14 27 3l23 11zM6 40h42M10 18v18M20 18v18M34 18v18M44 18v18"/></svg>Banking</div></div>
<div class="abs solution" style="left:839px;top:1939px"><div class="ring">
  <svg width="42" height="46" viewBox="0 0 42 46" fill="none" stroke="#fff" stroke-width="3"><path d="M21 3 39 9v14c0 11-8 17-18 20C11 40 3 34 3 23V9z"/><path d="m13 23 6 6 10-12"/></svg>Digital Identity<br>&amp; Security</div></div>

<!-- news -->
<h2 class="abs sec-title" style="top:2262px">Latest News</h2>
<svg class="abs" style="left:88px;top:2434px" width="28" height="44" viewBox="0 0 28 44" fill="none" stroke="#b8e986" stroke-width="3"><path d="M24 2 4 22l20 20"/></svg>
<svg class="abs" style="left:1085px;top:2434px" width="28" height="44" viewBox="0 0 28 44" fill="none" stroke="#b8e986" stroke-width="3"><path d="m4 2 20 20L4 42"/></svg>
<article class="abs news-card" style="left:150px;background:linear-gradient(180deg,#6aa0d8 0%,#f0a0c0 40%,#e04060 65%,#2a3060 100%)" role="img" aria-label="Light trails on a city highway at speed">
  <div class="date">19th October 2020</div>
  <div class="title">Lorem ipsum dolor sit amet, vero partem aliquando te quo, vis cu tempor legimus ocurreret..</div>
</article>
<article class="abs news-card" style="left:621px;background:linear-gradient(135deg,#0a1a5a,#123a9a 50%,#0a1550)" role="img" aria-label="Circuit board padlock graphic">
  <div class="date">19th October 2020</div>
  <div class="title">Ex duis dicat iusto mea. Illud delenit sapientem nam at, simul meliore his ei. Cum cu modus dolorum maiestatis.</div>
</article>
<a class="abs btn-solid" style="left:530px;top:2621px;width:140px;height:39px">See More »</a>

<!-- roadmap -->
<section class="band blue-b"></section>
<svg class="edge" style="top:2690px" viewBox="0 0 1200 60" preserveAspectRatio="none"><polygon fill="#22a53b" points="0,0 1200,0 1200,22 1150,14 1090,28 1030,18 970,30 910,16 850,26 790,12 730,24 670,10 610,22 550,14 490,28 430,16 370,30 310,20 250,32 190,18 130,28 70,16 0,24"/></svg>
<div class="abs map" role="img" aria-label="Faint world map"></div>
<h2 class="abs sec-title" style="top:2900px"><span>NORVEX</span> Roadmap</h2>

<div class="abs step" style="left:208px"><div class="when">Jan 2009</div><div class="what">Lorem ipsum dolor sit amet, vero partem aliquando te quo</div></div>
<div class="abs step" style="left:306px"><div class="when">June 2011</div><div class="what">Lorem ipsum dolor sit amet, vero partem aliquando te quo</div></div>
<div class="abs step" style="left:404px"><div class="when">June 2013</div><div class="what">Lorem ipsum dolor sit amet, vero partem aliquando te quo</div></div>
<div class="abs step" style="left:502px"><div class="when">June 2016</div><div class="what">Lorem ipsum dolor sit amet, vero partem aliquando te quo</div></div>
<div class="abs step" style="left:600px"><div class="when">Aug 2017</div><div class="what">Lorem ipsum dolor sit amet, vero partem aliquando te quo</div></div>
<div class="abs step" style="left:698px"><div class="when">May 2018</div><div class="what">Lorem ipsum dolor sit amet, vero partem aliquando te quo</div></div>
<div class="abs step" style="left:797px"><div class="when">May 2019</div><div class="what">Lorem ipsum dolor sit amet, vero partem aliquando te quo</div></div>
<div class="abs step" style="left:895px"><div class="when">Oct 2020</div><div class="what">Lorem ipsum dolor sit amet, vero partem aliquando te quo</div></div>

<div class="abs timeline"></div>
<div class="abs dot" style="left:152px"></div><div class="abs dot" style="left:249px"></div><div class="abs dot" style="left:347px"></div><div class="abs dot" style="left:446px"></div><div class="abs dot" style="left:544px"></div><div class="abs dot" style="left:642px"></div><div class="abs dot" style="left:740px"></div><div class="abs dot" style="left:839px"></div><div class="abs dot" style="left:937px"></div><div class="abs dot" style="left:1036px"></div>

<div class="abs badge" style="left:217px"><b></b></div>
<div class="abs badge" style="left:315px"><b></b></div>
<div class="abs badge" style="left:414px"><b></b></div>
<div class="abs badge" style="left:512px"><b></b></div>
<div class="abs badge" style="left:610px"><b></b></div>
<div class="abs badge" style="left:708px"><b></b></div>
<div class="abs badge" style="left:807px"><b></b></div>
<div class="abs badge" style="left:905px"><b></b></div>

<svg class="edge" style="top:3345px" viewBox="0 0 1200 60" preserveAspectRatio="none"><polygon fill="#22a53b" points="0,24 60,16 120,28 180,14 240,26 300,18 360,32 420,20 480,30 540,16 600,28 660,14 720,26 780,18 840,30 900,16 960,26 1020,12 1080,24 1140,16 1200,22 1200,60 0,60"/></svg>

<!-- certifications -->
<h2 class="abs sec-title" style="top:3441px">Our Certifications</h2>
<div class="abs cert" style="left:240px"><div class="mark"></div>SAS-UP</div>
<div class="abs cert" style="left:360px"><div class="mark"></div>SAS-SM</div>
<div class="abs cert" style="left:480px"><div class="mark round"></div>ISO 9001</div>
<div class="abs cert" style="left:600px"><div class="mark round"></div>ISO 27001</div>
<div class="abs cert" style="left:721px"><div class="mark round"></div>ISO 14001</div>
<div class="abs cert" style="left:836px"><div class="mark" style="height:20px;margin-top:19px;margin-bottom:29px"></div>CSA</div>

<!-- footer -->
<section class="band footer"></section>
<svg class="edge" style="top:3640px" viewBox="0 0 1200 60" preserveAspectRatio="none"><polygon fill="#22a53b" points="0,0 1200,0 1200,14 1140,22 1080,12 1020,24 960,16 900,28 840,18 780,26 720,14 660,24 600,16 540,28 480,18 420,26 360,14 300,22 240,12 180,24 120,16 60,22 0,14"/></svg>
<div class="abs fcol" style="left:148px"><h4>PRODUCTS</h4><a>SIM cards</a><a>RSP</a><a>Banking Cards</a><a>Digital Identity &amp; Security</a></div>
<div class="abs fcol" style="left:404px"><h4>SOLUTIONS</h4><a>RSP for OEMs</a><a>RSP for Telcos</a><a>RSP for MVNOs</a><a>MDM</a><a>OTA</a><a>QoS</a></div>
<div class="abs fcol" style="left:636px"><h4>ABOUT NORVEX</h4><a>Testimonials</a><a>Vision &amp; team</a><a>News</a><a>Videos</a><a>Visit us</a><a>Train with us</a><a>Contact</a></div>
<div class="abs fcol" style="left:861px"><h4>GET SOCIAL WITH US</h4></div>
<div class="abs social" style="left:867px;background:#2f5bb8"></div>
<div class="abs social" style="left:915px;background:#2a9be0"></div>
<div class="abs social" style="left:963px;background:#e0332b"></div>
<div class="abs social" style="left:1012px;background:#1a6ab8"></div>

<footer class="band bottom">
  <nav><a>FAQs</a><a>Terms</a><a>Privacy</a><a>Careers</a><a>Sitemap</a></nav>
  <div class="copy">Copyright © 1997-2020. Norvex Group. All rights reserved.</div>
</footer>

</body>
</html>
```